We would like a new design for our company Christmas Card. The design must have an orange background and have a festive theme.

The size of the card should be DL (210mm x 99mm).

Message on front cover: Merry Christmas
Message inside: Our warmest wishes for a wonderful Christmas and a very Happy New Year
From the team at under quiet rafters and tidal-crest

Please see attached example of the card that we used last year.

Industry/Entity Type

It Company

Colors
f78f20

Requirements
Must have
• Orange as the main colour
• A new design
• Font - Helevetica Neue Light (not condensed)

```html
<!DOCTYPE html>
<html lang="en">
<head>
<meta charset="utf-8">
<title>Merry Christmas – Team Card</title>
<link rel="stylesheet" href="https://fonts.googleapis.com/css2?family=Great+Vibes&family=Roboto:wght@300;400&display=swap">
<style>
  :root {
    --card-orange: #f78f20;
    --pine-dark: #1f3d1c;
    --pine-mid: #2f5a28;
    --pine-light: #4d7a3a;
    --title-white: #ffffff;
    --title-glow: #2f7d2a;
    --message-white: #fff8ee;
    --footer-ink: #111111;
    --gold-soft: #f2c23a;
    --gold-deep: #d99a12;
    --red-soft: #e8463a;
    --red-deep: #c21d16;
  }
  html, body {
    margin: 0;
    padding: 0;
    width: 1200px;
    height: 567px;
    overflow: hidden;
    background: var(--card-orange);
  }
  .card {
    position: relative;
    width: 1200px;
    height: 567px;
    background: var(--card-orange);
    overflow: hidden;
  }
  .card__decor {
    position: absolute;
    inset: 0;
    width: 1200px;
    height: 567px;
  }
  .card__title {
    position: absolute;
    top: 38px;
    left: 0;
    width: 1156px;
    margin: 0;
    text-align: center;
    font-family: "Great Vibes", cursive;
    font-weight: 400;
    font-size: 104px;
    line-height: 1.15;
    color: var(--title-white);
    text-shadow: 0 0 6px var(--title-glow), 0 0 3px var(--title-glow);
    white-space: nowrap;
  }
  .card__message {
    position: absolute;
    top: 258px;
    left: 30px;
    width: 1200px;
    margin: 0;
    text-align: center;
    font-family: "Roboto", "Helvetica Neue", sans-serif;
    font-weight: 300;
    font-size: 39px;
    line-height: 61px;
    color: var(--message-white);
    text-shadow: 0 1px 2px rgba(90, 40, 0, 0.35);
    white-space: nowrap;
  }
  .card__signoff {
    position: absolute;
    top: 474px;
    left: 292px;
    margin: 0;
    font-family: "Roboto", "Helvetica Neue", sans-serif;
    font-weight: 400;
    font-size: 20px;
    color: var(--footer-ink);
    white-space: nowrap;
  }
</style>
</head>
<body>
  <main class="card">
    <svg class="card__decor" viewBox="0 0 1200 567" xmlns="http://www.w3.org/2000/svg">
      <defs>
        <linearGradient id="pine-gradient" x1="0" y1="0" x2="1" y2="1">
          <stop offset="0" stop-color="var(--pine-mid)"/>
          <stop offset="0.5" stop-color="var(--pine-dark)"/>
          <stop offset="1" stop-color="var(--pine-light)"/>
        </linearGradient>
        <linearGradient id="gold-area" x1="0" y1="0" x2="0" y2="1">
          <stop offset="0" stop-color="var(--gold-soft)"/>
          <stop offset="1" stop-color="var(--gold-deep)"/>
        </linearGradient>
        <linearGradient id="red-area" x1="0" y1="0" x2="0" y2="1">
          <stop offset="0" stop-color="var(--red-soft)"/>
          <stop offset="1" stop-color="var(--red-deep)"/>
        </linearGradient>
      </defs>

      <path class="garland-frame" role="img" aria-label="Pine garland with holly leaves, red berries and small stars framing the card"
        fill="url(#pine-gradient)" fill-rule="evenodd"
        d="M0 0 H1200 V567 H0 Z
           M230 70
           C380 40 560 55 720 45
           C850 40 950 55 1010 80
           C1000 150 1040 220 1090 280
           C1070 350 1060 410 1010 460
           C880 500 760 515 620 510
           C480 505 330 500 200 485
           C140 440 110 390 120 330
           C110 260 100 200 150 130
           C170 100 200 80 230 70 Z"/>

      <rect class="ornament-area ornament-area--gold" role="img" aria-label="Gold Christmas bauble hanging on a thread"
        x="120" y="284" width="170" height="116" rx="18" fill="url(#gold-area)"/>

      <rect class="ornament-area ornament-area--red" role="img" aria-label="Red Christmas bauble with gold pattern hanging on a thread"
        x="870" y="444" width="164" height="123" rx="18" fill="url(#red-area)"/>
    </svg>

    <h1 class="card__title">Merry Christmas</h1>
    <p class="card__message">Our warmest wishes for a wonderful<br>Christmas and a very Happy New Year</p>
    <p class="card__signoff">From the team at under quiet rafters and tidal-crest</p>
  </main>
</body>
</html>
```